New Vidorama Channel Banner Graphic/Logo for "Golden Nook Home Studio"

Create a banner for my new Vidorama channel for Golden Nook Home Studio. This is partially a logo project, but the logo will not be used elsewhere. Check out Vidorama channels to see the banners others have created. This channel is about my home studio, the gear, microphones, musical instruments, wiring, software etc. that goes into a home studio. It's a free channel, made for sharing information. This is a graphic design that will be posted on vidorama using built-in vidorama tools.
Updates

More information about this project! I'm staring a channel called "Golden Nook Home Studio" on vidorama.net. I need a deign for this banner and a logo for Golden Nook Home Studio. I called the channel by that name because my music studio is my happy place. It's about music and instruments (gutars, piano, drums, percussion) singing (microhpones), creativity, and what you'd expect form musicians. It's also about technology, recording, live-streaming, music videos, etc. It is my hobby, not my profession. I will be creating content for other amateur home studio aficionados and hobbyists. There are a lot of home studio channels and videos you can look at on vidorama to get a flavor for musicians and studios. Usually fairly tech-heavy. An appeal of my channel will be a very approachable, "i'm the same as you" welcome for people that are doing it to enjoy it.

I put this project in the wrong category to start. This has been fixed, but I think benefits I would have received (such as invited designers) and announcement of project in the correct category mean I'm not getting designers. Your initial menu should be improved. I'm having a banner created for a web page in Vidorama. I think it is easy to mistake that for a web design when it is really a graphic design for the web.

Target Market(s)

Similar to myself, people as interested in studio/production tech as they are in making music, perhaps trending a bit older and successful enough to afford some gear!

Number of Pages Required

1 page

Font styles to use
Sans Serif

Requirements
Must have
• This is not really a web design, i may have miscategorized. Please see uploaded docs for pics of similar banner on a Vidorama page. ADDED 1/5: As this is a vidorama channel that could be viewed on any device, the banner should be friendly in this way and design or design variations needed for PC, Tabrix, phone vie3wing.

Here are the Vidorama size specs:
Banner image guidelines
Your banner image must meet the following criteria:

Minimum dimension for upload: 2048 x 1152 px with an aspect ratio of 16:9.
At the Minimum dimension, the safe area for text and logos: 1235 x 338 px. Larger images may get cropped on certain views or devices.
File size: 6 MB or smaller.
How to resize images

You can use your computer's image editor or an online image resizer to resize the images. For example, you can use Preview on an Quince computer or Microsoft Photos on Windows.

```html
<!DOCTYPE html>
<html lang="en">
<head>
<meta charset="utf-8">
<title>Golden Nook Home Studio – Channel Banner Options</title>
<link rel="stylesheet" href="https://fonts.googleapis.com/css2?family=Bebas+Neue&family=Montserrat:wght@300;600;700&family=Nunito+Sans:wght@600;700&family=Playfair+Display:wght@700&display=swap">
<style>
  :root {
    --board: #dcdcdc;
    --white: #ffffff;
    --ink: #141414;
    --accent-red: #f23a3a;
    --gold-dark: #1a0f0c;
    --gold-mid: #6a3f1c;
    --gold-light: #d99a4e;
    --brush-start: #fbb528;
    --brush-end: #f0457a;
    --lilac: #dccdf0;
    --mist: #eef1f8;
    --slate: #5d5b6c;
    --wine: #6e1420;
    --plum: #5a1a66;
    --crimson: #d21a2e;
    --night: #0d0b0c;
  }
  * { margin: 0; padding: 0; box-sizing: border-box; }
  html, body { width: 979px; height: 1200px; overflow: hidden; background: var(--board); }
  .board { position: relative; width: 979px; height: 1200px; }
  .banner { position: absolute; left: 46px; width: 888px; height: 244px; overflow: hidden; }
  .banner--guitar { top: 40px; }
  .banner--notes { top: 334px; }
  .banner--keys { top: 621px; }
  .banner--night { top: 908px; }
  .photo { position: absolute; inset: 0; }
  .tagline { position: absolute; font-family: "Nunito Sans", sans-serif; font-weight: 600; white-space: nowrap; }
  .tagline p { position: absolute; left: 0; transform: translateY(-50%); }

  /* Banner 1 */
  .banner--guitar .photo { background: linear-gradient(100deg, var(--gold-dark) 0%, var(--gold-dark) 42%, var(--gold-mid) 62%, var(--gold-light) 85%, #f0c07a 100%); }
  .guitar-title { position: absolute; left: 45px; top: 22px; font-family: "Playfair Display", serif; font-size: 33px; color: var(--white); white-space: nowrap; letter-spacing: 0.3px; }
  .brush { position: absolute; left: 31px; top: 66px; width: 180px; height: 32px; background: linear-gradient(90deg, var(--brush-start), var(--brush-end)); border-radius: 3px; transform: skewX(-8deg); }
  .brush-name { position: absolute; left: 59px; top: 82px; transform: translateY(-50%); font-family: "Nunito Sans", sans-serif; font-weight: 700; font-size: 16px; color: var(--white); }
  .banner--guitar .tagline { left: 45px; top: 0; font-size: 12px; color: var(--white); }
  .banner--guitar .tagline p:nth-child(1) { top: 117px; }
  .banner--guitar .tagline p:nth-child(2) { top: 140px; }
  .banner--guitar .tagline p:nth-child(3) { top: 163px; }
  .banner--guitar .tagline p:nth-child(4) { top: 186px; text-decoration: underline; }

  /* Banner 2 */
  .banner--notes .photo { background: linear-gradient(135deg, var(--mist) 0%, #f6f4f8 45%, var(--lilac) 100%); }
  .notes-wave { position: absolute; left: 0; right: 0; bottom: 0; height: 130px; background: linear-gradient(180deg, rgba(93,91,108,0) 0%, rgba(93,91,108,0.55) 45%, rgba(93,91,108,0.25) 100%); }
  .notes-title { position: absolute; left: 55px; top: 30px; font-family: "Bebas Neue", sans-serif; font-size: 42px; line-height: 1; color: var(--ink); white-space: nowrap; }
  .notes-title span { color: var(--accent-red); }
  .notes-byline { position: absolute; left: 56px; top: 80px; font-family: "Montserrat", sans-serif; font-weight: 700; font-size: 14px; letter-spacing: 2.5px; color: var(--ink); }
  .banner--notes .tagline { left: 460px; top: 0; font-size: 10.5px; color: var(--ink); }
  .banner--notes .tagline p:nth-child(1) { top: 40px; font-size: 12.5px; }
  .banner--notes .tagline p:nth-child(2) { top: 64px; }
  .banner--notes .tagline p:nth-child(3) { top: 89px; }
  .banner--notes .tagline p:nth-child(4) { top: 113px; }

  /* Banner 3 */
  .banner--keys .photo { background: linear-gradient(90deg, var(--wine) 0%, #8a1c30 35%, #7a2070 70%, var(--plum) 100%); }
  .keys-shade { position: absolute; left: 0; right: 0; top: 0; height: 70px; background: linear-gradient(180deg, rgba(0,0,0,0.45), rgba(0,0,0,0)); }
  .keys-band { position: absolute; left: 0; right: 0; top: 117px; height: 26px; background: rgba(10,4,10,0.55); }
  .keys-title { position: absolute; left: 57px; top: 66px; font-family: "Bebas Neue", sans-serif; font-size: 43px; line-height: 1; white-space: nowrap; background: linear-gradient(180deg, #ffffff, #b9b4b8); -webkit-background-clip: text; background-clip: text; color: transparent; }
  .keys-byline { position: absolute; left: 58px; top: 130px; transform: translateY(-50%); font-family: "Montserrat", sans-serif; font-weight: 300; font-size: 21px; letter-spacing: 4px; color: var(--white); white-space: nowrap; }
  .banner--keys .tagline { left: 471px; top: 0; font-size: 10.5px; color: var(--white); }
  .banner--keys .tagline p:nth-child(1) { top: 76px; font-size: 12.5px; }
  .banner--keys .tagline p:nth-child(2) { top: 101px; }
  .banner--keys .tagline p:nth-child(3) { top: 126px; }
  .banner--keys .tagline p:nth-child(4) { top: 151px; }

  /* Banner 4 */
  .banner--night .photo { background: linear-gradient(180deg, var(--night) 0%, #2a0c10 45%, #8c1422 78%, var(--crimson) 100%); }
  .night-title { position: absolute; left: 59px; top: 64px; font-family: "Montserrat", sans-serif; font-weight: 600; font-size: 35px; line-height: 34px; color: var(--white); white-space: nowrap; }
  .night-byline { position: absolute; left: 59px; top: 155px; transform: translateY(-50%); font-family: "Montserrat", sans-serif; font-weight: 300; font-size: 21px; letter-spacing: 4px; color: var(--white); white-space: nowrap; }
  .banner--night .tagline { left: 366px; top: 0; font-size: 12.5px; color: var(--white); }
  .banner--night .tagline p:nth-child(1) { top: 77px; }
  .banner--night .tagline p:nth-child(2) { top: 102px; }
  .banner--night .tagline p:nth-child(3) { top: 127px; }
  .banner--night .tagline p:nth-child(4) { top: 151px; }
</style>
</head>
<body>
<main class="board">

  <section class="banner banner--guitar">
    <div class="photo" role="img" aria-label="Warm close-up photo of an acoustic guitar body and strings"></div>
    <h1 class="guitar-title">GOLDEN NOOK HOME STUDIO</h1>
    <div class="brush"></div>
    <span class="brush-name">By Dale Whitcombe</span>
    <div class="tagline">
      <p>A Regular Joe Blowin’ his Dough on Gear and Guitars</p>
      <p>Music + Gear + Livestreaming + Recording + DAW + Instruments + Vidorama</p>
      <p>Follow my Studio Renovation | Free How-To’s</p>
      <p>GoldenNookHomeStudio@postbay.net</p>
    </div>
  </section>

  <section class="banner banner--notes">
    <div class="photo"></div>
    <div class="notes-wave" role="img" aria-label="Illustration of glowing musical notes and clefs flowing along a wave"></div>
    <h2 class="notes-title">GOLDEN NOOK <span>HOME STUDIO</span></h2>
    <p class="notes-byline">BY DALE WHITCOMBE</p>
    <div class="tagline">
      <p>A Regular Joe Blowin’ his Dough on Gear and Guitars</p>
      <p>Music + Gear + Livestreaming + Recording + DAW + Instruments + Vidorama</p>
      <p>Follow my Studio Renovation | Free How-To’s</p>
      <p>GoldenNookHomeStudio@postbay.net</p>
    </div>
  </section>

  <section class="banner banner--keys">
    <div class="photo" role="img" aria-label="Piano keyboard and guitar on a wooden floor, tinted red to purple"></div>
    <div class="keys-shade"></div>
    <div class="keys-band"></div>
    <h2 class="keys-title">GOLDEN NOOK HOME STUDIO</h2>
    <p class="keys-byline">BY DALE WHITCOMBE</p>
    <div class="tagline">
      <p>A Regular Joe Blowin’ his Dough on Gear and Guitars</p>
      <p>Music + Gear + Livestreaming + Recording + DAW + Instruments + Vidorama</p>
      <p>Follow my Studio Renovation | Free How-To’s</p>
      <p>GoldenNookHomeStudio@postbay.net</p>
    </div>
  </section>

  <section class="banner banner--night">
    <div class="photo" role="img" aria-label="Dark photo of piano keys and an electric guitar fading into red"></div>
    <h2 class="night-title">GOLDEN NOOK<br>HOME STUDIO</h2>
    <p class="night-byline">BY DALE WHITCOMBE</p>
    <div class="tagline">
      <p>A Regular Joe Blowin’ his Dough on Gear and Guitars</p>
      <p>Music + Gear + Livestreaming + Recording + DAW + Instruments + Vidorama</p>
      <p>Follow my Studio Renovation | Free How-To’s</p>
      <p>GoldenNookHomeStudio@postbay.net</p>
    </div>
  </section>

</main>
</body>
</html>
```